Letterhead design for Dental Practice - Ashby Lane Dental Care

Letterhead for Private Dental Practice. To be used for all official correspondance and for printing treatment details on to be given to patients.

Target Market(s)

Private dental patients

Industry/Entity Type

Dental Clinic

Font styles to use
Other font styles liked:
• nexa-light

Colors
33a6d7
1c66ac
85abd2

Requirements
Must have
• info in the footer and header needs to be 3.5cm from upper/lower boader of paper, see photo in uploaded files
• info details:
• tel. 0115 947 3051
• email info@ashbylanedc.co.uk
• ashbylanedentalcare.co.uk
• 17b Ashby Lane Elmsworth Harrowfield HF4 7QT
• nexa-light font as in uploaded logo files
Should not have
• No funny tooth pictures

```html
<!DOCTYPE html>
<html lang="en">
<head>
<meta charset="utf-8">
<title>Ashby Lane Dental Care – Letterhead</title>
<link href="https://fonts.googleapis.com/css2?family=Questrial&display=swap" rel="stylesheet">
<style>
  :root {
    --backdrop: #e8ebee;
    --paper: #ffffff;
    --brand-light: #33a6d7;
    --brand-deep: #1c66ac;
    --brand-soft: #85abd2;
    --ink: #3a3a3a;
    --contact-ink: #4a4a4a;
    --shadow: rgba(0, 0, 0, 0.12);
  }
  html, body {
    margin: 0;
    padding: 0;
    width: 1200px;
    height: 804px;
    overflow: hidden;
    background: var(--backdrop);
    font-family: "Questrial", "Helvetica Neue", Arial, sans-serif;
  }
  .canvas {
    position: relative;
    width: 1200px;
    height: 804px;
  }
  .letterhead {
    position: absolute;
    left: 316px;
    top: 12px;
    width: 568px;
    height: 780px;
    background: var(--paper);
    box-shadow: 0 4px 18px var(--shadow);
  }
  .brand {
    position: absolute;
    left: 46px;
    top: 60px;
    display: flex;
    align-items: center;
    gap: 10px;
  }
  .brand-dot {
    width: 22px;
    height: 22px;
    border-radius: 50%;
    background: var(--brand-light);
    flex: none;
  }
  .brand-name {
    font-size: 17px;
    color: var(--brand-deep);
    letter-spacing: 0.02em;
    line-height: 1;
    white-space: nowrap;
  }
  .letter-body {
    position: absolute;
    left: 232px;
    top: 132px;
    width: 292px;
    font-size: 9.5px;
    line-height: 1.55;
    color: var(--ink);
  }
  .letter-body p {
    margin: 0 0 14px;
  }
  .footer {
    position: absolute;
    left: 30px;
    right: 30px;
    bottom: 60px;
    text-align: center;
    font-size: 11px;
  }
  .contact-row {
    display: flex;
    justify-content: center;
    gap: 20px;
    margin-bottom: 8px;
    white-space: nowrap;
  }
  .contact-item {
    display: flex;
    align-items: center;
    gap: 6px;
    color: var(--contact-ink);
  }
  .contact-icon {
    width: 13px;
    height: 13px;
    flex: none;
  }
  .address {
    color: var(--brand-light);
    font-size: 11.5px;
    letter-spacing: 0.02em;
    white-space: nowrap;
  }
</style>
</head>
<body>
<div class="canvas">
  <article class="letterhead">
    <header class="brand">
      <span class="brand-dot"></span>
      <span class="brand-name">Ashby Lane Dental Care</span>
    </header>

    <section class="letter-body">
      <p>Thank you for choosing our practice for your dental care. This letter sets out the details of your recent visit and the treatment we have planned together. Please read it carefully and keep it with your records for future reference.</p>
      <p>Your next appointment will include a full check of your teeth and gums. If you have any questions about costs or timing, our reception team will be glad to help by phone or email.</p>
      <p>Please arrive ten minutes early so that we can update your medical history. If you need to change your booking, kindly give us at least one full day of notice. We look forward to seeing you soon.</p>
    </section>

    <footer class="footer">
      <div class="contact-row">
        <span class="contact-item">
          <svg class="contact-icon" viewBox="0 0 16 16" aria-hidden="true">
            <circle cx="8" cy="8" r="8" fill="var(--brand-light)"/>
            <path d="M5.4 4.2l1.3 1.6-.7 1a5 5 0 0 0 2.4 2.4l1-.7 1.6 1.3-.8 1.2C7.6 10.8 5.2 8.4 4.4 5z" fill="#fff"/>
          </svg>
          0115 947 3051
        </span>
        <span class="contact-item">
          <svg class="contact-icon" viewBox="0 0 16 16" aria-hidden="true">
            <circle cx="8" cy="8" r="8" fill="var(--brand-light)"/>
            <rect x="4" y="5.2" width="8" height="5.6" rx="0.6" fill="#fff"/>
            <path d="M4.3 5.5L8 8.3l3.7-2.8" stroke="var(--brand-light)" stroke-width="0.9" fill="none"/>
          </svg>
          info@ashbylanedc.co.uk
        </span>
        <span class="contact-item">
          <svg class="contact-icon" viewBox="0 0 16 16" aria-hidden="true">
            <circle cx="8" cy="8" r="8" fill="var(--brand-light)"/>
            <circle cx="8" cy="8" r="3.8" stroke="#fff" stroke-width="0.9" fill="none"/>
            <path d="M4.2 8h7.6M8 4.2c-1.6 2.2-1.6 5.4 0 7.6M8 4.2c1.6 2.2 1.6 5.4 0 7.6" stroke="#fff" stroke-width="0.8" fill="none"/>
          </svg>
          www.ashbylanedentalcare.co.uk
        </span>
      </div>
      <div class="address">17b Ashby Lane Elmsworth Harrowfield HF4 7QT</div>
    </footer>
  </article>
</div>
</body>
</html>
```